innovative design Cafe Menu

looking for an innovative design for a food menu for a coffee shop and take away restaurant.

Target Market(s)

Canada

Requirements
Must have
• innovative design and easy to navigate and reading

```html
<!DOCTYPE html>
<html lang="en">
<head>
<meta charset="utf-8">
<title>Cafe Menu</title>
<link rel="stylesheet" href="https://fonts.googleapis.com/css2?family=Bitter:wght@400;500;600&display=swap">
<style>
  :root{
    --green:#4c9f48;
    --green-text:#49a046;
    --deep-green:#0d4a20;
    --ink:#1e1e1e;
    --paper:#ffffff;
    --leader:#6b6b6b;
  }
  *{box-sizing:border-box;margin:0;padding:0}
  html,body{width:1200px;height:849px;overflow:hidden;background:var(--paper)}
  body{font-family:"Bitter",Georgia,serif;color:var(--ink)}
  .menu{position:relative;width:1200px;height:849px;overflow:hidden}
  .decor{position:absolute;inset:0;width:1200px;height:849px}
  .section{position:absolute;width:356px}
  .section-bar{background:var(--green);color:#fff;font-weight:600;font-size:14.5px;height:23px;line-height:23px;padding-left:8px}
  .items{list-style:none;padding:7px 0 0 8px}
  .item{margin-bottom:9px}
  .item-head{display:flex;align-items:baseline;height:17px}
  .item-name{color:var(--green-text);font-weight:500;font-size:14.5px;white-space:nowrap}
  .leader{flex:1;border-bottom:1px dotted var(--leader);margin:0 4px;transform:translateY(-3px)}
  .price{font-size:14px;white-space:nowrap}
  .item-desc{font-size:12px;line-height:15.8px;white-space:nowrap}
</style>
</head>
<body>
<main class="menu">
  <svg class="decor" viewBox="0 0 1200 849">
    <path role="img" aria-label="Photo of buffalo chicken wings on a plate with dipping sauces" d="M0 0 H545 C520 60 470 130 400 155 C340 176 300 165 240 170 C170 176 80 190 0 205 Z" fill="#cbb7a9"/>
    <path d="M0 0 H265 C220 30 180 45 150 70 C100 110 60 150 0 180 Z" fill="var(--deep-green)"/>

    <circle cx="666" cy="139" r="92" fill="none" stroke="var(--green)" stroke-width="5"/>
    <circle role="img" aria-label="Photo of chicken enchilada soup topped with sour cream and cilantro" cx="666" cy="139" r="85" fill="#b5593a"/>
    <circle cx="741" cy="191" r="18" fill="var(--deep-green)"/>
    <circle cx="736" cy="226" r="9" fill="var(--green)"/>
    <circle role="img" aria-label="Photo of a Greek salad with feta, tomato and olives" cx="546" cy="213" r="76" fill="#d8cfc4"/>

    <ellipse role="img" aria-label="Photo of a kofta wrap in flatbread" cx="538" cy="755" rx="100" ry="58" fill="#d9c9ad"/>
    <path role="img" aria-label="Photo of grilled kofta and chicken skewers with yellow rice and fries" d="M560 849 C620 760 700 670 800 640 C880 628 960 648 1040 640 C1110 632 1160 615 1200 605 V849 Z" fill="#6b4e35"/>
    <path d="M912 849 C960 770 1030 750 1100 735 C1150 724 1180 712 1200 705 V849 Z" fill="var(--deep-green)"/>
  </svg>

  <section class="section" style="left:22px;top:174px">
    <h2 class="section-bar">Sides</h2>
    <ul class="items">
      <li class="item"><div class="item-head"><span class="item-name">Crispy French Fries</span><span class="leader"></span><span class="price">$ 2.00</span></div><p class="item-desc">Crispy Flavoured Frech Fries</p></li>
      <li class="item"><div class="item-head"><span class="item-name">French Fries</span><span class="leader"></span><span class="price">$ 1.75</span></div><p class="item-desc">Straight Cut Fries</p></li>
      <li class="item"><div class="item-head"><span class="item-name">Buffalo Chiken Wings 5 Pcs.</span><span class="leader"></span><span class="price">$ 5.25</span></div><p class="item-desc">Juicy from inside crispy from outside<br>for of flavours</p></li>
      <li class="item"><div class="item-head"><span class="item-name">Buffalo Chiken Wings 10 Pcs.</span><span class="leader"></span><span class="price">$ 10.50</span></div><p class="item-desc">Juicy from inside crispy from outside<br>for of flavours</p></li>
      <li class="item"><div class="item-head"><span class="item-name">Honey Garlic Chicken Wings</span><span class="leader"></span><span class="price">$ 10.00</span></div></li>
      <li class="item"><div class="item-head"><span class="item-name">Fried Calamari</span><span class="leader"></span><span class="price">$ 6.99</span></div></li>
      <li class="item"><div class="item-head"><span class="item-name">Oriental Rice</span><span class="leader"></span><span class="price">$ 2.00</span></div><p class="item-desc">Flavourful rice short grain rice cooked<br>with onion, garlic and tomato</p></li>
    </ul>
  </section>

  <section class="section" style="left:22px;top:530px">
    <h2 class="section-bar">Wraps</h2>
    <ul class="items">
      <li class="item"><div class="item-head"><span class="item-name">Crispy Chicken</span><span class="leader"></span><span class="price">$ 6.99</span></div><p class="item-desc">Tender juicy peice of chicken marinated with our<br>im-house marination fried with a crispy tempura batter<br>serve with lettuce tomato cucumber pickles and mayo</p></li>
      <li class="item"><div class="item-head"><span class="item-name">Falafel</span><span class="leader"></span><span class="price">$ 4.99</span></div><p class="item-desc">Falafel is a deep-fried ball made from ground chickpeas<br>and fava beans. Served wrapped in a tortilla with<br>tahini sauce, lettuce, tomato and pickles</p></li>
      <li class="item"><div class="item-head"><span class="item-name">Grilled Chicken</span><span class="leader"></span><span class="price">$ 7.99</span></div><p class="item-desc">Tender juicy chicken pics marinated overnight was our<br>special marination made in the house laid over garlic<br>mayo lettuce and tomato and pickel wrap in tortilla</p></li>
      <li class="item"><div class="item-head"><span class="item-name">Kofta</span><span class="leader"></span><span class="price">$ 6.99</span></div><p class="item-desc">Barbeque ground beef our seasoning serve was the<br>tahini sauce pickle, lettuce and tomato</p></li>
    </ul>
  </section>

  <section class="section" style="left:422px;top:279px">
    <h2 class="section-bar">Salads</h2>
    <ul class="items">
      <li class="item"><div class="item-head"><span class="item-name">Greek Salad</span><span class="leader"></span><span class="price">$ 6.99</span></div><p class="item-desc">Tomato, sliced cucumber, green pepper, sliced<br>red onion, kalamata olives and of course feta cheese.<br>It must be seasoned with dried oregano and saslt<br>and dressed with good quality extra virgin olive oil<br>and a splash of red wine vinger.</p></li>
      <li class="item"><div class="item-head"><span class="item-name">Mediterranean Salad</span><span class="leader"></span><span class="price">$ 6.99</span></div><p class="item-desc">Chickpeas and tomato, sliced cucumber, green<br>pepper, sliced red onion, Kalamata olives and<br>feta cheese. It seasoned with salt and pepper<br>and simple vinaigrette dressing.</p></li>
      <li class="item"><div class="item-head"><span class="item-name">Avocado Salad</span><span class="leader"></span><span class="price">$ 7.99</span></div><p class="item-desc">Avocado, tomato, sliced cucumber, green pepper, sliced<br>red onion and cliantro seasoning with simple vinaigrette.<br>(Extra virgin olive oil &amp; white win vinegar)</p></li>
      <li class="item"><div class="item-head"><span class="item-name">Caesar Salad</span><span class="leader"></span><span class="price">$ 6.99</span></div><p class="item-desc">Romaine lettuce and croutons dressed with<br>Caesar dressing, Parmesan cheese and black pepper.</p></li>
    </ul>
  </section>

  <section class="section" style="left:822px;top:35px">
    <h2 class="section-bar">Soup</h2>
    <ul class="items">
      <li class="item"><div class="item-head"><span class="item-name">Chicken Enchilada Soup</span><span class="leader"></span><span class="price">$ 4.99</span></div><p class="item-desc">Is creamy, rich, slightly spicy and thick blended<br>together and topped with shredded chicken breast.</p></li>
      <li class="item"><div class="item-head"><span class="item-name">Mediterranean Salad</span><span class="leader"></span><span class="price">$ 4.99</span></div><p class="item-desc">Creamy broth with roasted chicken and<br>garlicky mushrooms.</p></li>
      <li class="item"><div class="item-head"><span class="item-name">Lentils Salad</span><span class="leader"></span><span class="price">$ 4.99</span></div><p class="item-desc">It’s vegetarian soup made use mix brown, red, yellow<br>lentils cooked with carrot, tomato and onion making<br>a thick soup with hint of Cayenne pepper.</p></li>
      <li class="item"><div class="item-head"><span class="item-name">French Onion Soup</span><span class="leader"></span><span class="price">$ 4.99</span></div><p class="item-desc">Made with perfectly caramelized onions, fresh thyme<br>springs, crustly baguette slices of melted Gruyere cheese<br>right on top</p></li>
    </ul>
  </section>

  <section class="section" style="left:822px;top:334px">
    <h2 class="section-bar">Platter</h2>
    <ul class="items">
      <li class="item"><div class="item-head"><span class="item-name">Kofta Platter</span><span class="leader"></span><span class="price">$ 12.80</span></div><p class="item-desc">Two kofta skewers servers with oriental rice + salad<br>or french fries and 1 sauce</p></li>
      <li class="item"><div class="item-head"><span class="item-name">Harvest Chicken Platter</span><span class="leader"></span><span class="price">$ 12.80</span></div><p class="item-desc">Two Harvest chicken skewers servers with<br>oriental rice + salad or french fries and 1 sauce.</p></li>
      <li class="item"><div class="item-head"><span class="item-name">Grilled Chicken Platter</span><span class="leader"></span><span class="price">$ 12.80</span></div><p class="item-desc">Two pieces of grilled chicken thigh and breast servers<br>with oriental rice + salad or french fries and 1 sauce.</p></li>
      <li class="item"><div class="item-head"><span class="item-name">Mix Grilled Platter</span><span class="leader"></span><span class="price">$ 25.99</span></div><p class="item-desc">Two Harvest chicken skewers + 2 skewers of kofta and<br>2 pieces of grilled chicken servers with oriental rice +<br>salad or french fries and 1 sauce.</p></li>
    </ul>
  </section>
</main>
</body>
</html>
```